Fotógrafo necesita portada completa para un libro de negocios enfocado a fotografía

Necesito la portada, contraportada y lomo de un libro de tapa blanda que venderé en Librovia llamado “Las claves para prosperar con la cámara”. Adjunto medidas requeridas por Librovia.

“Las claves para prosperar con la cámara” es un libro de negocios orientado a fotógrafos, no un libro de fotografía en sí mismo. Detallo las necesidades a continuación:

- Descripción general: Necesito que el diseño sea llamativo, pero lo suficientemente sencillo, moderno y atractivo como para que el cliente perciba en el diseño que el interior contiene un gran valor. No quiero elementos recargados ni diseños muy complicados de entender. Para más inspiración, ver las portadas de libros como "Las mañas del pudiente", "La mente del capital", "rutinas mínimas", siguiendo el estilo de mi marca personal: www.rodrigovelmar.com
- Portada: La portada debe expresar sensaciones de emoción y libertad (al emprender un negocio fotográfico de la forma que transmito en el interior del libro), pero también de misterio (debido a esos “secretos” para vivir del negocio de la fotografía)
- Contraportada: dividida en dos secciones: Una para la breve descripción del libro y otra para la descripción de la biografía del autor con foto.

Por último, necesito el diseño editable en .PSD con los textos provisionales “lorem ipsum”, ya que todavía no tengo los textos definitivos y seré yo quien los integre, así que aprovecharé esos campos de texto, con la fuente, tamaño y color para hacerlo.

Target Market(s)

Photographers

Industry/Entity Type

Photography, economy, marketing

Font styles to use
Serif
Sans Serif

Requirements
Must have
• Title: Las claves para prosperar con la cámara (Capital or not. Depending on design), Subtitle: El manual completo para trabajar con tu cámara sin perder la cabeza en el camino. Author: Rodrigo Velmar
Should not have
• pictures, photos, ¿gradients?

```html
<!DOCTYPE html>
<html lang="es">
<head>
<meta charset="utf-8">
<title>Las claves para prosperar con la cámara — cubierta completa</title>
<link href="https://fonts.googleapis.com/css2?family=Bebas+Neue&family=Montserrat:ital,wght@0,500;1,500&family=Arimo&display=swap" rel="stylesheet">
<style>
  :root {
    --paper: #e6e1d6;
    --ink-red: #7c170c;
    --bright-red: #b01414;
    --slate: #3c3f48;
    --body-grey: #4d4d4f;
    --spine-black: #000000;
    --barcode-white: #ffffff;
  }
  * { margin: 0; padding: 0; box-sizing: border-box; }
  html, body { width: 1200px; height: 865px; overflow: hidden; background: var(--paper); }
  .cover { position: relative; width: 1200px; height: 865px; background: var(--paper); overflow: hidden; }

  /* Back cover */
  .back-title {
    position: absolute; left: 82px; top: 22px;
    font-family: "Bebas Neue", sans-serif; font-weight: 400; font-size: 36px; line-height: 38.5px;
    color: var(--ink-red);
  }
  .back-emblem { position: absolute; left: 308px; top: 40px; width: 128px; height: 96px; }
  .rule { position: absolute; background: var(--ink-red); }
  .rule--back-top { left: 56px; top: 151px; width: 462px; height: 5px; }
  .rule--back-bottom { left: 56px; top: 554px; width: 462px; height: 5px; }
  .synopsis {
    position: absolute; left: 56px; top: 186px; width: 468px;
    font-family: "Arimo", sans-serif; font-size: 15.6px; line-height: 17.6px;
    color: var(--body-grey);
  }
  .synopsis p + p { margin-top: 17.6px; }
  .author-bio {
    position: absolute; left: 56px; top: 590px; width: 260px;
    font-family: "Montserrat", sans-serif; font-style: italic; font-weight: 500;
    font-size: 12.2px; line-height: 14.4px; color: var(--ink-red);
  }
  .barcode-area { position: absolute; left: 360px; top: 725px; width: 194px; height: 117px; background: var(--barcode-white); }

  /* Spine */
  .spine { position: absolute; left: 577px; top: 0; width: 46px; height: 865px; background: var(--spine-black); }
  .spine-title, .spine-author {
    position: absolute; left: 50%; white-space: nowrap; color: var(--paper);
    transform-origin: 0 0; transform: rotate(90deg) translateY(-50%);
  }
  .spine-title { top: 55px; font-family: "Bebas Neue", sans-serif; font-size: 31px; line-height: 1; }
  .spine-author { top: 606px; font-family: "Montserrat", sans-serif; font-weight: 500; font-size: 23px; line-height: 1; }

  /* Front cover */
  .front { position: absolute; left: 623px; top: 0; width: 577px; height: 865px; }
  .front-title { font-family: "Bebas Neue", sans-serif; font-weight: 400; color: var(--ink-red); }
  .front-title span {
    position: absolute; left: 0; width: 577px; text-align: center;
    display: block; line-height: 1; white-space: nowrap;
  }
  .front-title .line-lead { top: 40px; font-size: 98px; }
  .front-title .line-mid { top: 139px; font-size: 55px; color: var(--bright-red); }
  .front-title .line-main { top: 194px; font-size: 100px; }
  .rule--sub-top { left: 93px; top: 315px; width: 387px; height: 4px; }
  .rule--sub-bottom { left: 93px; top: 398px; width: 387px; height: 4px; }
  .subtitle {
    position: absolute; left: 0; top: 334px; width: 577px; text-align: center;
    font-family: "Bebas Neue", sans-serif; font-size: 24px; line-height: 29px; color: var(--slate);
  }
  .cover-art { position: absolute; left: 139px; top: 430px; width: 302px; height: 302px; }
  .author-name {
    position: absolute; left: 0; top: 772px; width: 577px; text-align: center;
    font-family: "Montserrat", sans-serif; font-weight: 500; font-size: 42px; line-height: 1;
    color: var(--slate); letter-spacing: 1px;
  }
</style>
</head>
<body>
<main class="cover">
  <section class="back">
    <h2 class="back-title">LAS CLAVES<br>PARA PROSPERAR<br>CON LA CÁMARA</h2>
    <svg class="back-emblem" viewBox="0 0 128 96" role="img" aria-label="Ilustración de una cámara réflex en gris">
      <rect width="128" height="96" rx="6" fill="#a9a79e"/>
    </svg>
    <div class="rule rule--back-top"></div>
    <div class="synopsis">
      <p>Lorem ipsum dolor sit amet consectetur adipiscing elit condimentum donec ac laoreet suscipit nostra volutpat, euismod ad tempus himenaeos turpis sodales gravida morbi nec cras congue enim. Luctus hendrerit netus curae eu imperdiet vivamus tempus donec diam praesent, nullam cursus mi odio integer elementum quis ac semper faucibus nibh, taciti leo libero sociis porta laoreet aenean malesuada euismod. Bibendum pulvinar metus convallis ad porta consequat at accumsan senectus rutrum quis, tincidunt diam class ac justo tempor fames habitant non.</p>
      <p>Quis pharetra iaculis phasellus torquent viverra convallis lacinia gravida ridiculus sociis vel diam, risus luctus tincidunt arcu potenti habitasse sodales vivamus vehicula feugiat hac. Sociosqu dis euismod primis blandit pulvinar eleifend potenti dignissim dictum mattis fermentum ullamcorper vitae, augue congue egestas ultrices purus felis nam feugiat odio commodo auctor. Nulla cras tincidunt pretium lectus orci curabitur per parturient imperdiet, ornare dis euismod vivamus malesuada a sed vestibulum metus justo, faucibus nunc sollicitudin lobortis aliquet torquent non varius.</p>
    </div>
    <div class="rule rule--back-bottom"></div>
    <p class="author-bio">Lorem ipsum dolor sit amet consectetur adipiscing elit condimentum donec ac laoreet suscipit nostra volutpat, euismod ad tempus himenaeos turpis sodales gravida morbi nec cras congue enim. Luctus hendrerit netus curae eu imperdiet vivamus tempus donec diam praesent, nullam cursus mi odio integer elementum quis ac semper faucibus nibh, taciti leo libero sociis porta laoreet aenean malesuada euismod. Bibendum pulvinar metus convallis ad porta consequat at accumsan senectus rutrum quis, tincidunt diam class ac justo tempor fames habitant non.</p>
    <div class="barcode-area"></div>
  </section>

  <aside class="spine">
    <span class="spine-title">LAS CLAVES PARA PROSPERAR CON LA CÁMARA</span>
    <span class="spine-author">RODRIGO VELMAR</span>
  </aside>

  <section class="front">
    <h1 class="front-title">
      <span class="line-lead">LAS CLAVES</span>
      <span class="line-mid">PARA PROSPERAR</span>
      <span class="line-main">CON LA CÁMARA</span>
    </h1>
    <div class="rule rule--sub-top"></div>
    <p class="subtitle">EL MANUAL COMPLETO PARA TRABAJAR CON TU<br>CÁMARA SIN PERDER LA CABEZA EN EL CAMINO</p>
    <div class="rule rule--sub-bottom"></div>
    <svg class="cover-art" viewBox="0 0 302 302" role="img" aria-label="Ilustración circular de una cámara sobre trípode ante un paisaje de montañas rojizas bajo un cielo nocturno, enmarcada en un aro oscuro">
      <defs>
        <linearGradient id="art-tone" x1="0" y1="0" x2="0" y2="1">
          <stop offset="0" stop-color="#c8514b"/>
          <stop offset="0.55" stop-color="#e48a7c"/>
          <stop offset="1" stop-color="#3a2b2d"/>
        </linearGradient>
      </defs>
      <circle cx="151" cy="151" r="151" fill="#2a2a2e"/>
      <circle cx="151" cy="151" r="128" fill="url(#art-tone)"/>
    </svg>
    <p class="author-name">RODRIGO VELMAR</p>
  </section>
</main>
</body>
</html>
```